Business Card and Letterhead Design for Public Accounting Firm

Business card and letterhead design for a CPA Firm located in Orange County, CA. We're looking for a modern and professional design utilizing our existing logo. We'd like a clean "less is more" look, but also something that catches the eye. We provide a high level of service to our clients. Open to single or double sided business cards.

Additional info: color numbers on logo
Blue :
R 0
G 83
B 125

#00537D

Silver :

R 154
G 154
B 154

#9A9A9A

Target Market(s)

Businesses and individuals

Industry/Entity Type

Accounting

Contact Information for Business Card

Hewitt Dansby & Mortlake LLP - 4726 Larkspur Hollow Road, Irvine, CA 92614 - (949)382-7146 - hdmledgers.example

Font styles to use
Serif
Sans Serif
Other font styles liked:
• See font file uploaded

Colors
0054AA
0677BA
7BADD7
CADEEF
E8F1F8

Requirements
Nice to have
• Possibly use the font file provided which matches our logo, but adjust to be not in all caps

```html
<!DOCTYPE html>
<html lang="en">
<head>
<meta charset="utf-8">
<title>Hewitt Dansby &amp; Mortlake LLP — Business Card</title>
<link rel="stylesheet" href="https://fonts.googleapis.com/css2?family=Cinzel:wght@400&family=EB+Garamond:wght@400&display=swap">
<style>
  :root {
    --brand-blue: #00537D;
    --card-blue: #055682;
    --deboss-blue: #044a71;
    --silver: #9A9A9A;
    --paper: #ffffff;
    --backdrop: #e3e3e1;
    --ink-muted: #8a8a8a;
  }
  * { margin: 0; padding: 0; box-sizing: border-box; }
  html, body { width: 1200px; height: 801px; overflow: hidden; }
  body {
    background: var(--backdrop);
    display: flex;
    align-items: center;
    justify-content: center;
    gap: 60px;
    font-family: "EB Garamond", Georgia, serif;
  }
  .card {
    width: 500px;
    height: 286px;
    position: relative;
    box-shadow: 0 2px 6px rgba(0,0,0,0.12);
  }
  .card--front { background: var(--paper); border-bottom: 3px solid var(--brand-blue); }
  .card--back { background: var(--card-blue); }

  .brand {
    position: absolute;
    display: flex;
    align-items: center;
    gap: 16px;
  }
  .brand__mark {
    width: 48px; height: 48px;
    border-radius: 50%;
    background: var(--brand-blue);
    flex: none;
  }
  .brand__rule { width: 1px; height: 62px; background: var(--silver); }
  .brand__name {
    font-family: "Cinzel", "Times New Roman", serif;
    font-size: 19px;
    line-height: 1.2;
    letter-spacing: 0.06em;
    color: var(--silver);
    text-transform: uppercase;
  }

  .card--front .brand { left: 70px; top: 62px; }

  .card--back .brand { left: 80px; top: 104px; }
  .card--back .brand__mark { background: var(--deboss-blue); }
  .card--back .brand__rule { background: var(--deboss-blue); }
  .card--back .brand__name { color: #2f7fb3; }

  .contact {
    position: absolute;
    left: 0; right: 0;
    top: 176px;
    display: flex;
    justify-content: center;
    align-items: center;
    gap: 18px;
    color: var(--ink-muted);
    font-size: 16px;
    line-height: 1.35;
  }
  .contact__address { text-align: right; }
  .contact__rule { width: 1px; height: 44px; background: var(--silver); }
  .contact__lines { list-style: none; }
  .contact__lines li { display: flex; align-items: center; gap: 7px; }
  .contact__icon { width: 11px; height: 11px; flex: none; }
</style>
</head>
<body>
  <section class="card card--front" aria-label="Business card front">
    <div class="brand">
      <span class="brand__mark"></span>
      <span class="brand__rule"></span>
      <p class="brand__name">Hewitt Dansby<br>&amp; Mortlake LLP</p>
    </div>
    <div class="contact">
      <address class="contact__address" style="font-style:normal">
        4726 Larkspur Hollow Road<br>Irvine, CA 92614
      </address>
      <span class="contact__rule"></span>
      <ul class="contact__lines">
        <li>
          <svg class="contact__icon" viewBox="0 0 12 12" aria-hidden="true"><circle cx="6" cy="6" r="6" fill="#00537D"/><path d="M3.6 3.2l1.3-.4.7 1.6-.8.6c.4.9 1 1.5 1.9 1.9l.6-.8 1.6.7-.4 1.3C6 8.3 3.7 6 3.6 3.2z" fill="#fff"/></svg>
          (949) 382-7146
        </li>
        <li>
          <svg class="contact__icon" viewBox="0 0 12 12" aria-hidden="true"><circle cx="6" cy="6" r="6" fill="#00537D"/><circle cx="6" cy="6" r="3.6" fill="none" stroke="#fff" stroke-width="0.8"/><path d="M2.4 6h7.2M6 2.4c-1.6 2-1.6 5.2 0 7.2M6 2.4c1.6 2 1.6 5.2 0 7.2" fill="none" stroke="#fff" stroke-width="0.6"/></svg>
          hdmledgers.example
        </li>
      </ul>
    </div>
  </section>

  <section class="card card--back" aria-label="Business card back">
    <div class="brand">
      <span class="brand__mark"></span>
      <span class="brand__rule"></span>
      <p class="brand__name">Hewitt Dansby<br>&amp; Mortlake LLP</p>
    </div>
  </section>
</body>
</html>
```